Velora Aesthetica

Medical doctor providing aesthetic medicine

* Double sided card
* Logo to be on card
Other details:
* Dr. Mirela Kostvan, BSc, MBChB, CCFP
* #214-215, 27903 83 Ave, Surrey, BC, V2T 4K7
* 604-718-2943
* info@veloraclinic.ca
* www.veloraclinic.ca

Industry/Entity Type

Medical / Health & Beauty

Contact Information for Business Card

see 'Project Description'

Colors
0054AA
0677BA
7BADD7
CADEEF
E8F1F8
FFF300
FFF600
FEFA6F
FFFEC7
FFFEE8

Requirements
Must have
• Modern, high-end design

```html
<!DOCTYPE html>
<html lang="en">
<head>
<meta charset="utf-8">
<title>Velora Aesthetica – Business Card</title>
<link href="https://fonts.googleapis.com/css2?family=Montserrat:wght@500;600&family=Roboto:wght@500;700&display=swap" rel="stylesheet">
<style>
  :root {
    --page: #ffffff;
    --card-navy: #22425f;
    --accent-gold: #d9b43a;
    --accent-blue: #1aa3d4;
    --text-white: #ffffff;
  }
  * { box-sizing: border-box; margin: 0; padding: 0; }
  html, body {
    width: 967px; height: 1200px; overflow: hidden;
    background: var(--page);
  }
  .sheet { position: relative; width: 967px; height: 1200px; }
  .card {
    position: absolute; left: 260px; width: 446px; height: 274px;
    background: var(--card-navy);
  }
  .card--front { top: 314px; }
  .card--back { top: 611px; }

  .brand {
    position: absolute; display: flex; flex-direction: column; align-items: center;
    transform: translate(-50%, -50%);
  }
  .brand__dot {
    border: 1.5px solid var(--accent-gold); border-radius: 50%;
  }
  .brand__name {
    font-family: "Montserrat", sans-serif; font-weight: 500;
    color: var(--text-white); text-transform: uppercase; white-space: nowrap;
  }
  .card--front .brand { left: 110px; top: 140px; }
  .card--front .brand__dot { width: 40px; height: 40px; margin-bottom: 10px; }
  .card--front .brand__name { font-size: 11px; letter-spacing: 2.4px; }
  .card--back .brand { left: 223px; top: 140px; }
  .card--back .brand__dot { width: 70px; height: 70px; margin-bottom: 16px; }
  .card--back .brand__name { font-size: 18px; letter-spacing: 4px; }

  .contact {
    position: absolute; left: 193px; top: 62px;
    font-family: "Roboto", Arial, sans-serif; color: var(--text-white);
  }
  .contact__name {
    font-size: 21px; font-weight: 700; color: var(--accent-blue);
    line-height: 1; margin-bottom: 8px;
  }
  .contact__details { font-size: 13px; font-weight: 700; line-height: 15px; margin-bottom: 9px; }
  .contact__list { list-style: none; }
  .contact__item {
    display: flex; align-items: center; gap: 4px;
    font-size: 16px; font-weight: 700; line-height: 20px; height: 21px;
  }
  .icon {
    width: 17px; height: 17px; border-radius: 3px;
    display: flex; align-items: center; justify-content: center; flex: none;
  }
  .icon--gold { background: var(--accent-gold); }
  .icon--blue { background: var(--accent-blue); }
  .icon svg { width: 12px; height: 12px; }
</style>
</head>
<body>
<main class="sheet">
  <section class="card card--front">
    <div class="brand">
      <span class="brand__dot"></span>
      <span class="brand__name">Velora Aesthetica</span>
    </div>
    <div class="contact">
      <p class="contact__name">Dr. Mirela Kostvan</p>
      <p class="contact__details">BSc, MBChB, CCFP<br>214-215, 27903 83 Ave<br>Surrey, BC, V2T 4K7</p>
      <ul class="contact__list">
        <li class="contact__item">
          <span class="icon icon--gold"><svg viewBox="0 0 24 24"><path fill="#fff" d="M6.6 10.8a15 15 0 0 0 6.6 6.6l2.2-2.2c.3-.3.7-.4 1-.2 1.1.4 2.3.6 3.6.6.6 0 1 .4 1 1V20c0 .6-.4 1-1 1A17 17 0 0 1 3 4c0-.6.4-1 1-1h3.5c.6 0 1 .4 1 1 0 1.3.2 2.5.6 3.6.1.3 0 .7-.2 1z"/></svg></span>
          604-718-2943
        </li>
        <li class="contact__item">
          <span class="icon icon--blue"><svg viewBox="0 0 24 24"><rect x="3" y="5" width="18" height="14" rx="2" fill="none" stroke="#fff" stroke-width="2"/><path d="M3 7l9 6 9-6" fill="none" stroke="#fff" stroke-width="2"/></svg></span>
          info@veloraclinic.ca
        </li>
        <li class="contact__item">
          <span class="icon icon--gold"><svg viewBox="0 0 24 24"><circle cx="12" cy="12" r="9" fill="none" stroke="#fff" stroke-width="2"/><path d="M3 12h18M12 3c3 3 3 15 0 18M12 3c-3 3-3 15 0 18" fill="none" stroke="#fff" stroke-width="1.6"/></svg></span>
          www.veloraclinic.ca
        </li>
      </ul>
    </div>
  </section>

  <section class="card card--back">
    <div class="brand">
      <span class="brand__dot"></span>
      <span class="brand__name">Velora Aesthetica</span>
    </div>
  </section>
</main>
</body>
</html>
```